Stationary design for IT Consultancy
Stationary Design (Business Cards - Letter Heads - Envelopes - Presentation Folders - Power Point)
Stationary design for IT Consultancy - Information Technology
Creative Brief
Use standard fonts
Optional fonts can be used
Professional
Dean Marlow
Technical Director
14 Brindle Works Oakfield Lane Stoneham Wexshire WX7 2QP
dean.marlow@pivotal-nsg.net
www.pivotal-nsg.net

```html
<!DOCTYPE html>
<html lang="en">
<head>
<meta charset="utf-8">
<title>Pivotal Network Systems Group — Stationery</title>
<link href="https://fonts.googleapis.com/css2?family=Montserrat:wght@400;500;600;800&display=swap" rel="stylesheet">
<style>
  :root {
    --brand-blue: #3d5bb5;
    --brand-blue-light: #6f86cc;
    --paper: #ffffff;
    --backdrop: #e8e9ec;
    --ink: #5a5f6b;
  }
  * { margin: 0; padding: 0; box-sizing: border-box; }
  html, body { width: 1200px; height: 936px; overflow: hidden; }
  body {
    background: var(--backdrop);
    font-family: "Montserrat", Arial, sans-serif;
    color: var(--ink);
    position: relative;
  }
  .piece {
    position: absolute;
    background: var(--paper);
    overflow: hidden;
    box-shadow: 0 1px 3px rgba(0,0,0,0.12);
  }
  .piece > svg.curves { position: absolute; inset: 0; width: 100%; height: 100%; }
  .wordmark {
    position: absolute;
    color: var(--brand-blue);
    font-weight: 800;
    letter-spacing: 0.06em;
    line-height: 1;
    display: flex;
    align-items: center;
    gap: 0.35em;
    white-space: nowrap;
  }
  .wordmark .mark-square {
    width: 0.8em; height: 0.8em; background: var(--brand-blue); display: inline-block;
  }
  .descriptor {
    position: absolute;
    color: var(--brand-blue);
    font-weight: 800;
    letter-spacing: 0.22em;
    white-space: nowrap;
    line-height: 1;
  }
  .small-print {
    position: absolute;
    font-size: 5px;
    line-height: 1.5;
    color: var(--ink);
  }

  /* Letterhead */
  .letterhead { left: 183px; top: 63px; width: 388px; height: 551px; }
  .letterhead .wordmark { left: 30px; top: 30px; font-size: 13px; }
  .letterhead .descriptor { left: 52px; top: 46px; font-size: 4.5px; }
  .letterhead .small-print { left: 250px; top: 24px; width: 80px; }

  /* Presentation folder */
  .folder { left: 634px; top: 38px; width: 462px; height: 579px; }
  .folder .wordmark { left: 0; right: 0; justify-content: center; top: 268px; font-size: 36px; }
  .folder .descriptor { left: 0; right: 0; text-align: center; top: 314px; font-size: 10px; }

  /* Business cards */
  .card-front { left: 43px; top: 655px; width: 180px; height: 98px; border-radius: 6px; }
  .card-front .wordmark { left: 16px; top: 20px; font-size: 10px; }
  .card-front .descriptor { left: 32px; top: 33px; font-size: 3.5px; }
  .card-front .small-print { left: 16px; top: 48px; font-size: 4.5px; }
  .card-front .person-name { font-weight: 600; color: var(--brand-blue); }
  .card-back { left: 43px; top: 766px; width: 180px; height: 97px; border-radius: 6px; background: var(--brand-blue); }
  .card-back .card-web {
    position: absolute; left: 0; right: 0; bottom: 12px; text-align: center;
    color: #fff; font-size: 5px; letter-spacing: 0.2em; text-transform: uppercase;
  }

  /* Envelope front */
  .envelope-front { left: 261px; top: 667px; width: 437px; height: 211px; }
  .envelope-front .wordmark { left: 22px; top: 22px; font-size: 12px; }
  .envelope-front .descriptor { left: 42px; top: 37px; font-size: 4px; }
  .envelope-front .small-print { left: 22px; top: 50px; width: 140px; }

  /* Envelope back */
  .envelope-back { left: 736px; top: 672px; width: 426px; height: 203px; }
  .envelope-back .flap-web {
    position: absolute; left: 0; right: 0; top: 30px; text-align: center;
    color: #fff; font-size: 9px; letter-spacing: 0.3em; text-transform: uppercase; font-weight: 500;
  }
</style>
</head>
<body>

  <section class="piece letterhead" aria-label="Letterhead">
    <svg class="curves" viewBox="0 0 388 551" preserveAspectRatio="none" aria-hidden="true">
      <path d="M318 0 C350 30 372 80 388 160 L388 0 Z" fill="var(--brand-blue)"/>
      <path d="M300 0 C340 35 368 95 388 190" fill="none" stroke="var(--brand-blue)" stroke-width="1.2"/>
      <path d="M0 410 C15 470 45 520 85 551 L0 551 Z" fill="var(--brand-blue)"/>
      <path d="M0 385 C20 460 60 525 110 551" fill="none" stroke="var(--brand-blue)" stroke-width="1.2"/>
    </svg>
    <div class="wordmark"><span class="mark-square"></span>PIVOTAL</div>
    <div class="descriptor">NETWORK SYSTEMS GROUP</div>
    <div class="small-print">
      14 Brindle Works Oakfield Lane<br>Stoneham Wexshire WX7 2QP<br>T: +44 1632 960418<br>dean.marlow@pivotal-nsg.net<br>www.pivotal-nsg.net
    </div>
  </section>

  <section class="piece folder" aria-label="Presentation folder">
    <svg class="curves" viewBox="0 0 462 579" preserveAspectRatio="none" aria-hidden="true">
      <path d="M395 0 C425 45 448 110 462 210 L462 0 Z" fill="var(--brand-blue)"/>
      <path d="M378 0 C415 55 444 130 462 240" fill="none" stroke="var(--brand-blue)" stroke-width="1.4"/>
      <path d="M0 420 C18 490 50 545 95 579 L0 579 Z" fill="var(--brand-blue)"/>
      <path d="M0 390 C22 480 68 548 122 579" fill="none" stroke="var(--brand-blue)" stroke-width="1.4"/>
    </svg>
    <div class="wordmark"><span class="mark-square"></span>PIVOTAL</div>
    <div class="descriptor">NETWORK SYSTEMS GROUP</div>
  </section>

  <section class="piece card-front" aria-label="Business card front">
    <svg class="curves" viewBox="0 0 180 98" preserveAspectRatio="none" aria-hidden="true">
      <path d="M150 0 C165 25 174 60 180 98 L180 0 Z" fill="var(--brand-blue)"/>
      <path d="M142 0 C160 30 171 65 175 98" fill="none" stroke="var(--brand-blue)" stroke-width="0.8"/>
    </svg>
    <div class="wordmark"><span class="mark-square"></span>PIVOTAL</div>
    <div class="descriptor">NETWORK SYSTEMS GROUP</div>
    <div class="small-print">
      <span class="person-name">Dean Marlow</span><br>Technical Director<br>dean.marlow@pivotal-nsg.net
    </div>
  </section>

  <section class="piece card-back" aria-label="Business card back">
    <div class="card-web">www.pivotal-nsg.net</div>
  </section>

  <section class="piece envelope-front" aria-label="Envelope front">
    <svg class="curves" viewBox="0 0 437 211" preserveAspectRatio="none" aria-hidden="true">
      <path d="M400 0 C418 50 430 120 437 211 L437 0 Z" fill="var(--brand-blue)"/>
      <path d="M388 0 C410 55 424 130 430 211" fill="none" stroke="var(--brand-blue)" stroke-width="1"/>
    </svg>
    <div class="wordmark"><span class="mark-square"></span>PIVOTAL</div>
    <div class="descriptor">NETWORK SYSTEMS GROUP</div>
    <div class="small-print">
      14 Brindle Works Oakfield Lane Stoneham<br>Wexshire WX7 2QP · www.pivotal-nsg.net
    </div>
  </section>

  <section class="piece envelope-back" aria-label="Envelope back">
    <svg class="curves" viewBox="0 0 426 203" preserveAspectRatio="none" aria-hidden="true">
      <path d="M0 0 L426 0 L426 70 C300 78 130 78 0 70 Z" fill="var(--brand-blue)"/>
    </svg>
    <div class="flap-web">www.pivotal-nsg.net</div>
  </section>

</body>
</html>
```